Business Card desgin, company called Tall Orbit.

I am looking for the logo colors (3) to be used on the card in whatever design you think might work. the certifications are on the back (4) on the front will be my name, Dana Whitlock, owner/instructor, phone 317.582.4096, website www.tlo-coaching.example, email dw@tlo-coaching.example. im flexible on fonts.

Target Market(s)

firearms owners

Industry/Entity Type

firearms training

Contact Information for Business Card

certification icons on back

```html
<!DOCTYPE html>
<html lang="en">
<head>
<meta charset="utf-8">
<title>Tall Orbit – Business Card</title>
<link rel="stylesheet" href="https://fonts.googleapis.com/css2?family=Montserrat:wght@700;800&family=Open+Sans:wght@400;600&family=Libre+Baskerville&display=swap">
<style>
  :root {
    --navy: #0c2840;
    --navy-deep: #09213a;
    --red: #c4262c;
    --white: #f3f4f6;
    --placeholder: #24415c;
    --page: #e6e4e0;
  }
  * { margin: 0; padding: 0; box-sizing: border-box; }
  html, body { width: 1200px; height: 900px; overflow: hidden; }
  body {
    background: var(--page);
    font-family: "Open Sans", sans-serif;
    position: relative;
  }
  .card {
    position: absolute;
    left: 250px;
    width: 700px;
    height: 400px;
    background: linear-gradient(135deg, var(--navy) 0%, var(--navy-deep) 100%);
    box-shadow: 0 8px 24px rgba(0,0,0,.25);
    overflow: hidden;
  }
  .card--back { top: 35px; }
  .card--front { top: 465px; }

  .brand {
    display: flex; align-items: center; gap: 12px;
    font-family: "Montserrat", sans-serif;
    font-weight: 800;
    color: var(--red);
    text-transform: uppercase;
    white-space: nowrap;
  }
  .brand__dot {
    width: 22px; height: 22px; border-radius: 50%;
    background: var(--red);
  }

  /* Back */
  .card--back .brand { position: absolute; left: 48px; top: 70px; font-size: 34px; letter-spacing: 1px; }
  .card--back .site {
    position: absolute; left: 84px; top: 126px;
    font-family: "Montserrat", sans-serif; font-weight: 700;
    color: var(--white); font-size: 13px; letter-spacing: 1px;
  }
  .certifications {
    position: absolute; left: 150px; bottom: 46px;
    display: flex; align-items: flex-end; gap: 26px;
  }
  .certification {
    width: 76px; height: 76px;
    border-radius: 8px;
    background: var(--placeholder);
  }

  /* Front */
  .card--front .brand { position: absolute; right: 48px; top: 46px; font-size: 32px; letter-spacing: 1px; }
  .card--front .site {
    position: absolute; right: 48px; top: 92px;
    font-family: "Libre Baskerville", serif;
    color: var(--white); font-size: 17px;
    white-space: nowrap;
  }
  .divider {
    position: absolute; left: 270px; right: 40px; top: 252px;
    height: 1px; background: var(--red);
  }
  .person { position: absolute; left: 48px; top: 226px; }
  .person__name {
    font-weight: 600; color: var(--white); font-size: 22px;
    text-transform: uppercase; letter-spacing: .3px; line-height: 1.1;
  }
  .person__role { color: var(--red); font-size: 17px; margin-top: 2px; }
  .contacts { list-style: none; margin-top: 16px; }
  .contacts li {
    display: flex; align-items: center; gap: 12px;
    color: var(--white); font-size: 16px; line-height: 1.7;
    white-space: nowrap;
  }
  .contacts svg { width: 16px; height: 16px; flex: none; }
</style>
</head>
<body>

<section class="card card--back" aria-label="Card back">
  <div class="brand"><span class="brand__dot"></span>Tall Orbit</div>
  <div class="site">WWW.TLO-COACHING.EXAMPLE</div>
  <div class="certifications">
    <div class="certification" role="img" aria-label="Range safety officer certification"></div>
    <div class="certification" role="img" aria-label="Firearms instructor certification"></div>
    <div class="certification" role="img" aria-label="Tactical instructor certification"></div>
    <div class="certification" role="img" aria-label="Concealed carry instructor certification"></div>
  </div>
</section>

<section class="card card--front" aria-label="Card front">
  <div class="brand"><span class="brand__dot"></span>Tall Orbit</div>
  <div class="site">WWW.TLO-Coaching.example</div>
  <div class="divider"></div>
  <div class="person">
    <h1 class="person__name">Dana Whitlock</h1>
    <p class="person__role">Owner/Instructor</p>
    <ul class="contacts">
      <li>
        <svg viewBox="0 0 24 24" aria-hidden="true"><path fill="var(--red)" d="M6.6 10.8a15.2 15.2 0 0 0 6.6 6.6l2.2-2.2a1 1 0 0 1 1-.25 11.4 11.4 0 0 0 3.6.57 1 1 0 0 1 1 1V20a1 1 0 0 1-1 1A17 17 0 0 1 3 4a1 1 0 0 1 1-1h3.5a1 1 0 0 1 1 1c0 1.25.2 2.45.57 3.57a1 1 0 0 1-.25 1z"/></svg>
        317.582.4096
      </li>
      <li>
        <svg viewBox="0 0 24 24" aria-hidden="true"><rect x="2" y="5" width="20" height="14" rx="1" fill="var(--red)"/><path d="M2 6 L12 13 L22 6" fill="none" stroke="var(--navy)" stroke-width="1.8"/></svg>
        dw@tlo-coaching.example
      </li>
      <li>
        <svg viewBox="0 0 24 24" aria-hidden="true" fill="none" stroke="var(--red)" stroke-width="1.8"><circle cx="12" cy="12" r="9.5"/><ellipse cx="12" cy="12" rx="4" ry="9.5"/><path d="M2.5 12h19M4 7h16M4 17h16"/></svg>
        www.tlo-coaching.example
      </li>
    </ul>
  </div>
</section>

</body>
</html>
```